Business Cards

The name of our firm is "Bayfield Insurance adjusters"
We separate ourselves from all other public adjusters because most of us worked for the insurance companies so we understand their games.
As Insurance adjusters we represent the Insured, not the insurance companies. Our # 1 priority is to handle the entire claim process as seamless as possible on behalf of the homeowner/business owner so they don't have to deal with the hassles and headaches. Just as the logo your team designed, I want the cards to stand out from everyone elses. I also want the cards to help better understand our services and Value on hiring us and value that we can offer.
I uploaded the logo whenever I created the project. I don't see an option on re uploading the logo anywhere. Any advise??

```html
<!DOCTYPE html>
<html lang="en">
<head>
<meta charset="utf-8">
<title>Bayfield Insurance Adjusters – Business Card</title>
<link href="https://fonts.googleapis.com/css2?family=Open+Sans:wght@400;600;700;800&display=swap" rel="stylesheet">
<style>
  :root {
    --canvas: #e4e4e4;
    --navy: #08466b;
    --navy-soft: #0d5580;
    --brand-blue: #1a6fa5;
    --paper: #f4f4f4;
    --ink: #444444;
    --ink-soft: #555555;
    --rule: #2a7bb0;
  }
  * { margin: 0; padding: 0; box-sizing: border-box; }
  html, body {
    width: 1200px; height: 960px; overflow: hidden;
    background: var(--canvas);
    font-family: "Open Sans", Arial, sans-serif;
  }
  .canvas { position: relative; width: 1200px; height: 960px; }
  .card {
    position: absolute; top: 185px;
    width: 340px; height: 595px;
    overflow: hidden;
  }
  .card--back { left: 234px; background: var(--navy); }
  .card--front { left: 626px; background: var(--paper); }

  .back-wordmark {
    position: absolute; left: 0; right: 0; top: 370px;
    text-align: center;
    color: var(--navy-soft);
    font-weight: 800;
    line-height: 1.1;
  }
  .back-wordmark .name { display: block; font-size: 36px; letter-spacing: 1px; }
  .back-wordmark .tag { display: block; font-size: 13px; letter-spacing: 1.5px; }

  .front-band { position: absolute; left: 0; top: 0; width: 340px; height: 180px; }

  .front-wordmark {
    position: absolute; left: 0; right: 0; top: 225px;
    text-align: center;
    color: var(--brand-blue);
    font-weight: 800;
    line-height: 1.1;
  }
  .front-wordmark .name { display: block; font-size: 34px; letter-spacing: 1px; }
  .front-wordmark .tag { display: block; font-size: 12px; letter-spacing: 1.5px; }

  .person { position: absolute; left: 0; right: 0; top: 375px; text-align: center; }
  .person__name { font-size: 18px; font-weight: 700; color: var(--brand-blue); letter-spacing: 0.5px; }
  .person__role { font-size: 14px; color: var(--ink-soft); margin-top: 1px; }

  .contact-rule { position: absolute; left: 72px; top: 441px; width: 194px; height: 20px; }

  .contact { position: absolute; left: 0; right: 0; top: 471px; text-align: center; font-size: 14.5px; line-height: 20px; color: var(--ink); }
  .contact strong { color: var(--brand-blue); font-weight: 700; }
</style>
</head>
<body>
<main class="canvas">
  <section class="card card--back" aria-label="Card back">
    <p class="back-wordmark">
      <span class="name">BAYFIELD</span>
      <span class="tag">INSURANCE ADJUSTERS</span>
    </p>
  </section>

  <section class="card card--front" aria-label="Card front">
    <svg class="front-band" viewBox="0 0 340 180" aria-hidden="true">
      <polygon points="0,0 340,0 340,180 170,37 0,180" fill="var(--navy)"/>
    </svg>

    <p class="front-wordmark">
      <span class="name">BAYFIELD</span>
      <span class="tag">INSURANCE ADJUSTERS</span>
    </p>

    <div class="person">
      <p class="person__name">DANIEL ORSINI</p>
      <p class="person__role">President</p>
    </div>

    <svg class="contact-rule" viewBox="0 0 194 20" aria-hidden="true">
      <line x1="0" y1="10" x2="194" y2="10" stroke="var(--rule)" stroke-width="1.5"/>
      <!-- phone -->
      <circle cx="72" cy="10" r="9" fill="var(--brand-blue)"/>
      <path d="M68 6 l2 -1 l1.6 3 l-1.2 1 q1 2.2 3 3 l1 -1.2 l3 1.6 l-1 2 q-6 0 -8.4 -8.4z" fill="#fff"/>
      <!-- mail -->
      <circle cx="98" cy="10" r="9" fill="var(--brand-blue)"/>
      <rect x="92.5" y="6" width="11" height="8" fill="none" stroke="#fff" stroke-width="1.3"/>
      <polyline points="92.5,6 98,10.5 103.5,6" fill="none" stroke="#fff" stroke-width="1.3"/>
      <!-- web -->
      <circle cx="123" cy="10" r="9" fill="var(--brand-blue)"/>
      <circle cx="123" cy="10" r="5.5" fill="none" stroke="#fff" stroke-width="1.2"/>
      <ellipse cx="123" cy="10" rx="2.3" ry="5.5" fill="none" stroke="#fff" stroke-width="1"/>
      <line x1="117.5" y1="10" x2="128.5" y2="10" stroke="#fff" stroke-width="1"/>
    </svg>

    <div class="contact">
      <p>321-555-0147</p>
      <p>daniel@bayfieldinad.com</p>
      <p>www.<strong>bayfieldinad</strong>.com</p>
    </div>
  </section>
</main>
</body>
</html>
```